Migration Lawyers

Company: Thornbury & Co Lawyers & Migration Agents

Name: Gavin Rusholt BEc, LLB
Address: Level 19, 71 Pelham Street
Sydney, NSW, Australia 2000

Ph: +61 2 9357 2164
M: 0438261504
E: gavin@permit-nomadra.org.au
W: www.permit-nomadra.org.au

Target Market(s)

Migration Clients

Industry/Entity Type

It Company

Font styles to use
Script

Requirements
Must have
• Logo
Should not have
• Please scale the format to the printing size attached

```html
<!DOCTYPE html>
<html lang="en">
<head>
<meta charset="utf-8">
<title>Thornbury &amp; Co — Business Cards</title>
<link rel="stylesheet" href="https://fonts.googleapis.com/css2?family=Tinos:wght@400;700&family=Open+Sans:wght@400&display=swap">
<style>
  :root {
    --bg: #e9e6e1;
    --card: #ffffff;
    --ink: #111111;
    --black: #0b0b0b;
    --red: #e3120b;
    --grey: #4a4a4a;
    --faint: #e4e4e4;
    --white: #ffffff;
  }
  * { margin: 0; padding: 0; box-sizing: border-box; }
  html, body { width: 1200px; height: 1136px; overflow: hidden; background: var(--bg); }
  .canvas { position: relative; width: 1200px; height: 1136px; }

  .card {
    position: absolute;
    width: 881px; height: 503px;
    background: var(--card);
    border-radius: 38px;
    overflow: hidden;
    box-shadow: 0 6px 18px rgba(0,0,0,0.25);
  }
  .card-front { left: 21px; top: 37px; }
  .card-back  { left: 276px; top: 599px; }

  .front-art { position: absolute; inset: 0; width: 100%; height: 100%; }

  .brand-mark {
    position: absolute; left: 58px; top: 70px;
    width: 140px; height: 140px; border-radius: 50%;
    border: 3px solid #d5d5d5;
  }
  .brand-name {
    position: absolute; left: 222px; top: 104px;
    font-family: "Tinos", "Times New Roman", serif;
    font-weight: 700; color: var(--ink);
    line-height: 1.1;
  }
  .brand-name .firm { display: block; font-size: 44px; }
  .brand-name .trade { display: block; font-size: 22px; margin-top: 4px; }

  .person { position: absolute; left: 42px; top: 284px; font-family: "Tinos", "Times New Roman", serif; }
  .person-name { font-size: 28px; font-weight: 700; color: var(--ink); }
  .person-quals { font-size: 23px; color: var(--grey); margin-top: 4px; }

  .contact-list {
    position: absolute; right: 24px; top: 286px;
    list-style: none; text-align: right;
    font-family: "Open Sans", Arial, sans-serif; font-size: 19px; color: var(--white);
  }
  .contact-list li { height: 37.5px; display: flex; align-items: center; justify-content: flex-end; gap: 8px; }
  .contact-list svg { width: 18px; height: 18px; flex: none; }

  .office-address {
    position: absolute; right: 42px; top: 454px;
    font-family: "Open Sans", Arial, sans-serif; font-size: 18px; color: var(--white);
  }

  .back-ring {
    position: absolute; left: 273px; top: 61px;
    width: 360px; height: 360px; border-radius: 50%;
    border: 6px solid var(--faint);
  }
  .back-brand {
    position: absolute; left: 0; right: 0; top: 170px; text-align: center;
    font-family: "Tinos", "Times New Roman", serif; font-weight: 700; color: var(--ink);
    line-height: 1.1;
  }
  .back-brand .firm { display: block; font-size: 84px; }
  .back-brand .trade { display: block; font-size: 36px; margin-top: 6px; }
  .back-web {
    position: absolute; left: 0; right: 0; top: 446px; text-align: center;
    font-family: "Open Sans", Arial, sans-serif; font-size: 22px; letter-spacing: 2px; color: #222;
  }
</style>
</head>
<body>
<main class="canvas">

  <section class="card card-front" aria-label="Business card front">
    <svg class="front-art" viewBox="0 0 574 328" preserveAspectRatio="none" aria-hidden="true">
      <path d="M540,0 L574,0 L574,328 L0,328 L0,268 C130,318 330,290 430,190 C480,135 515,70 540,0 Z" fill="var(--black)"/>
      <path d="M0,242 C40,282 140,300 230,272 C300,250 360,215 405,180 C360,228 300,268 230,290 C140,314 40,300 0,262 Z" fill="var(--red)"/>
    </svg>

    <div class="brand-mark" aria-hidden="true"></div>
    <div class="brand-name">
      <span class="firm">Thornbury &amp; Co</span>
      <span class="trade">Lawyers &amp; Migration Agents</span>
    </div>

    <div class="person">
      <p class="person-name">Gavin Rusholt</p>
      <p class="person-quals">BEc, LLB</p>
    </div>

    <ul class="contact-list">
      <li>
        <svg viewBox="0 0 20 20" aria-hidden="true"><circle cx="10" cy="10" r="9" fill="#fff"/><path d="M6.5 5.5l2 2-1 1.3c.7 1.5 1.8 2.6 3.3 3.3l1.3-1 2 2-1.3 1.6c-3.6-.4-7.2-4-7.6-7.6z" fill="#000"/></svg>
        <span>+61 2 9357 2164</span>
      </li>
      <li>
        <svg viewBox="0 0 20 20" aria-hidden="true"><rect x="5" y="2" width="10" height="16" rx="2" fill="#fff"/><rect x="7" y="4" width="6" height="9" fill="#000"/></svg>
        <span>0438261504</span>
      </li>
      <li>
        <svg viewBox="0 0 20 20" aria-hidden="true"><rect x="2" y="5" width="16" height="11" rx="2" fill="#fff"/><path d="M3 6l7 5 7-5" stroke="#000" stroke-width="1.5" fill="none"/></svg>
        <span>gavin@permit-nomadra.org.au</span>
      </li>
      <li>
        <svg viewBox="0 0 20 20" aria-hidden="true"><circle cx="10" cy="10" r="8.5" fill="#fff"/><g stroke="#000" stroke-width="1.2" fill="none"><ellipse cx="10" cy="10" rx="3.5" ry="7.5"/><path d="M2.5 10h15M4 6h12M4 14h12"/></g></svg>
        <span>www.permit-nomadra.org.au</span>
      </li>
    </ul>

    <p class="office-address">Level 19, 71 Pelham Street, Australia, Sydney, NSW, 2000</p>
  </section>

  <section class="card card-back" aria-label="Business card back">
    <div class="back-ring" aria-hidden="true"></div>
    <div class="back-brand">
      <span class="firm">Thornbury &amp; Co</span>
      <span class="trade">Lawyers &amp; Migration Agents</span>
    </div>
    <p class="back-web">www.permit-nomadra.org.au</p>
  </section>

</main>
</body>
</html>
```